The Harwood Bellamy Firm

We are a real estate and business acquisition services company that provides consulting services to large companies and individuals. The company provided nationwide services to companies looking to expand through opening new locations or buying other companies in their field. We work very close with attorneys, accountants, banks/financial institutions and high level executives and business owners.

Target Market(s)

CEO, VP, business owners and bankers.

Industry/Entity Type

Real Estate

Requirements
Must have
• I am looking for a design that looks very professional and has a classic, trustworthy, professional feeling. I want the letterhead and return address to look formal and official so this it is not tossed out as junk mail. HB or HBF can be used in a logo style part but that is not required. Our tag line is "Real Estate and Business Acquisition Services". This should be on the letter head but not on the return address. It does not need a lot of color but I will leave that to your tasteful choice. It should be rich and formal looking.
Should not have
• I do not want anything that looks like a cartoon drawing or figure. Use font that gives a strong trustworthy look. We are not a law firm so no scales or gavels. A law firm sort of look or feel is OK.

```html
<!DOCTYPE html>
<html lang="en">
<head>
<meta charset="utf-8">
<title>The Harwood Bellamy Firm – Letterhead</title>
<link rel="stylesheet" href="https://fonts.googleapis.com/css2?family=Marcellus&family=Jura:wght@500&display=swap">
<style>
  :root {
    --paper: #ffffff;
    --frame: #2f5656;
    --ink: #111111;
    --rule: #5a6b70;
    --bubble: #d3eaf2;
    --card-top: #e9f4f7;
    --card-bottom: #a9d2dd;
    --card-edge: #2c3436;
    --card-ink: #1f2b30;
    --mark: #1e2a30;
    --mark-dot: #7fa8d6;
  }
  html, body {
    margin: 0;
    padding: 0;
    overflow: hidden;
    background: var(--paper);
  }
  .sheet {
    position: relative;
    width: 928px;
    height: 1200px;
    overflow: hidden;
    background: var(--paper);
  }
  .scroll-frame {
    position: absolute;
    inset: 0;
  }
  .brand-mark {
    position: absolute;
    left: 58px;
    top: 100px;
    display: flex;
    align-items: center;
    gap: 8px;
    font-family: "Marcellus", serif;
    font-size: 34px;
    line-height: 1;
    color: var(--mark);
    transform: rotate(-28deg);
    transform-origin: left center;
  }
  .brand-mark .dot,
  .card-mark .dot {
    border-radius: 50%;
    background: var(--mark-dot);
  }
  .brand-mark .dot {
    width: 12px;
    height: 12px;
  }
  .tagline {
    position: absolute;
    left: 0;
    width: 928px;
    top: 90px;
    margin: 0;
    text-align: center;
    font-family: "Marcellus", serif;
    font-weight: 400;
    font-size: 44px;
    line-height: 57px;
    letter-spacing: 1px;
    color: var(--ink);
  }
  .business-card {
    position: absolute;
    left: 276px;
    top: 470px;
    width: 425px;
    height: 224px;
    border-radius: 10px;
    border: 3px solid var(--card-edge);
    background: linear-gradient(160deg, var(--card-top), var(--card-bottom));
    box-shadow: 4px 6px 10px rgba(0,0,0,0.35);
    transform: rotate(-14deg);
    box-sizing: border-box;
  }
  .card-mark {
    position: absolute;
    left: 24px;
    top: 70px;
    display: flex;
    align-items: center;
    gap: 6px;
    font-family: "Marcellus", serif;
    font-size: 28px;
    line-height: 1;
    color: var(--mark);
    transform: rotate(-22deg);
  }
  .card-mark .dot {
    width: 10px;
    height: 10px;
  }
  .card-address {
    position: absolute;
    right: 28px;
    top: 44px;
    margin: 0;
    text-align: center;
    font-family: "Marcellus", serif;
    font-style: normal;
    font-size: 15px;
    line-height: 21px;
    color: var(--card-ink);
  }
  .return-address {
    position: absolute;
    left: 580px;
    width: 300px;
    top: 980px;
    margin: 0;
    text-align: center;
    font-family: "Jura", sans-serif;
    font-weight: 500;
    font-style: normal;
    font-size: 17px;
    line-height: 25.5px;
    color: var(--ink);
  }
</style>
</head>
<body>
<div class="sheet">
  <svg class="scroll-frame" width="928" height="1200" viewBox="0 0 928 1200" aria-hidden="true">
    <rect x="21" y="32" width="882" height="1138" rx="3" fill="none" stroke="var(--frame)" stroke-width="3"/>
    <path d="M150 92 C 360 74, 640 72, 850 84 C 880 86, 890 100, 872 112" fill="none" stroke="var(--frame)" stroke-width="3"/>
    <path d="M62 150 C 70 400, 72 700, 66 1060 C 64 1095, 56 1115, 62 1120" fill="none" stroke="var(--frame)" stroke-width="2.5"/>
    <path d="M842 110 C 848 400, 852 700, 856 955" fill="none" stroke="var(--frame)" stroke-width="3"/>
    <path d="M60 1115 C 40 1128, 56 1142, 90 1140 C 330 1138, 600 1130, 868 1120" fill="none" stroke="var(--frame)" stroke-width="3"/>
    <path d="M128 210 C 350 205, 600 204, 776 206" fill="none" stroke="var(--rule)" stroke-width="1.5"/>
    <circle cx="100" cy="207" r="24" fill="var(--bubble)" stroke="#b8d5e0" stroke-width="1"/>
    <path d="M620 968 C 585 964, 565 973, 575 988 C 585 1040, 585 1090, 588 1130" fill="none" stroke="#8a9499" stroke-width="1.5"/>
    <path d="M620 968 C 700 958, 780 954, 840 958" fill="none" stroke="#8a9499" stroke-width="1.5"/>
    <path d="M398 782 C 500 765, 590 750, 668 725" fill="none" stroke="#9aa4a8" stroke-width="1.2"/>
  </svg>

  <div class="brand-mark"><span class="dot"></span>HBF</div>

  <h1 class="tagline">Real Estate And<br>Business Acquisition Services</h1>

  <div class="business-card">
    <div class="card-mark"><span class="dot"></span>HBF</div>
    <address class="card-address">
      The Harwood Bellamy Firm<br>
      4120 Cedar Ridge Pike, Suite<br>
      Brookdale, TN 37400<br>
      615-555-0148<br>
      www.harwoodbellamy.com
    </address>
  </div>

  <address class="return-address">
    The Harwood Bellamy Firm<br>
    4120 Cedar Ridge Pike, Suite<br>
    Brookdale, TN 37400<br>
    615-555-0148<br>
    www.harwoodbellamy.com
  </address>
</div>
</body>
</html>
```